Stonebell Inc Ad Design, trying to attract new customers

Please see attached pictures and files for information
We are a Class A - Residential General Contractor in Lynchburg, VA with Master HVAC and Master PLUMBING Licenses. We focus on Water and Air Solutions for property owners.
We build, remodel, and repair homes
We do HVAC, including Humidity Control and Air Purification
We do Plumbing
We love to fix Water Leaks for Plumbing, Roof Leaks, Skylight Leaks, Basement Leaks, Foundation Leaks, Door and Window Leaks
We solve water and air issues on the outside of properties with custom structures, grading, and landscaping

Target Market(s)

Residential and Light Commercial property owners

Industry/Entity Type

Construction

Font styles to use
Other font styles liked:
• see cards

Colors
0054AA
0677BA
7BADD7
CADEEF
E8F1F8
00AB8E
00BBA5
67D7C9
C6EFE9
E9F9F6

Requirements
Must have
• See business cards
Nice to have
• see business cards
Should not have
• My name

```html
<!DOCTYPE html>
<html lang="en">
<head>
<meta charset="utf-8">
<title>Stonebell Inc – Water &amp; Air Solutions Banner</title>
<link rel="stylesheet" href="https://fonts.googleapis.com/css2?family=Poppins:wght@600;700;800;900&display=swap">
<style>
  :root {
    --stage: #e6e6e6;
    --ink: #333a40;
    --headline: #1f97dc;
    --headline-deep: #3b98d8;
    --headline-shadow: rgba(20, 60, 100, 0.55);
    --brand-blue: #0677BA;
    --navy: #0054AA;
    --sky: #7BADD7;
    --mist: #CADEEF;
    --ice: #E8F1F8;
    --pill: #8fd0f5;
    --dot: #6cc4f2;
    --tick: #2f9be0;
    --white: #ffffff;
  }

  * { box-sizing: border-box; margin: 0; padding: 0; }

  html, body {
    width: 1200px;
    height: 720px;
    overflow: hidden;
    background: var(--stage);
    font-family: "Poppins", sans-serif;
  }

  .banner {
    position: absolute;
    left: 0;
    top: 60px;
    width: 1200px;
    height: 600px;
    overflow: hidden;
    background: linear-gradient(100deg, #ffffff 0%, #f7fafd 30%, var(--ice) 45%, #a9d3f1 65%, #5eaee6 85%, #4a9fdc 100%);
  }

  .banner__backdrop {
    position: absolute;
    inset: 0;
    background:
      radial-gradient(ellipse 60% 70% at 40% 55%, rgba(202, 222, 239, 0.35), transparent 70%);
  }

  .banner__worker {
    position: absolute;
    right: 0;
    top: 0;
    width: 470px;
    height: 600px;
    background:
      radial-gradient(ellipse 55% 60% at 62% 55%, rgba(70, 150, 220, 0.55), transparent 75%),
      linear-gradient(90deg, rgba(90, 170, 230, 0) 0%, rgba(70, 155, 225, 0.5) 40%, rgba(60, 145, 215, 0.65) 100%);
  }

  .brand {
    position: absolute;
    left: 0;
    width: 780px;
    top: 78px;
    display: flex;
    justify-content: center;
    align-items: center;
    gap: 10px;
  }

  .brand__mark {
    width: 22px;
    height: 22px;
    border-radius: 50%;
    background: var(--brand-blue);
  }

  .brand__name {
    font-weight: 800;
    font-size: 30px;
    letter-spacing: 1px;
    color: var(--brand-blue);
  }

  .headline {
    position: absolute;
    left: 0;
    width: 780px;
    text-align: center;
    font-weight: 900;
    text-transform: uppercase;
    letter-spacing: -1.5px;
    line-height: 1;
    text-shadow: 2px 4px 4px var(--headline-shadow);
  }

  .headline--question {
    top: 131px;
    left: 44px;
    width: auto;
    font-size: 62px;
    color: var(--headline);
  }

  .headline--promise {
    top: 193px;
    left: 139px;
    width: auto;
    font-size: 74px;
    color: var(--headline-deep);
  }

  .services {
    position: absolute;
    left: 52px;
    top: 273px;
    list-style: none;
  }

  .services__item {
    display: flex;
    align-items: center;
    height: 40.5px;
    font-weight: 600;
    font-size: 20px;
    color: var(--ink);
  }

  .services__tick {
    width: 28px;
    height: 28px;
    margin-right: 17px;
    flex: none;
    filter: drop-shadow(0 2px 2px rgba(0, 0, 0, 0.35));
  }

  .area {
    position: absolute;
    left: 189px;
    top: 485px;
    width: 250px;
    height: 32px;
    border-radius: 16px;
    background: var(--pill);
    box-shadow: 0 0 10px 3px rgba(120, 200, 245, 0.8);
    display: flex;
    align-items: center;
    justify-content: center;
    font-weight: 700;
    font-size: 19px;
    color: var(--navy);
  }

  .licenses {
    position: absolute;
    top: 534px;
    left: 0;
    width: 700px;
    height: 26px;
    list-style: none;
  }

  .licenses__item {
    position: absolute;
    top: 0;
    display: flex;
    align-items: center;
    height: 26px;
    font-weight: 600;
    font-size: 18px;
    color: var(--ink);
  }

  .licenses__item::before {
    content: "";
    width: 20px;
    height: 20px;
    border-radius: 50%;
    background: var(--dot);
    margin-right: 15px;
  }

  .licenses__item--class { left: 53px; }
  .licenses__item--hvac { left: 185px; }
  .licenses__item--plumbing { left: 376px; }

  .phone {
    position: absolute;
    left: 661px;
    top: 505px;
    display: flex;
    align-items: center;
    gap: 20px;
  }

  .phone__icon {
    width: 68px;
    height: 68px;
    flex: none;
    filter: drop-shadow(0 3px 3px rgba(0, 0, 0, 0.3));
  }

  .phone__number {
    font-weight: 700;
    font-size: 55px;
    line-height: 1;
    color: var(--white);
    letter-spacing: 0.5px;
    text-shadow: 2px 3px 4px rgba(0, 30, 70, 0.6);
  }
</style>
</head>
<body>
  <section class="banner">
    <div class="banner__backdrop" role="img" aria-label="Faded photograph of a two-storey suburban house"></div>
    <div class="banner__worker" role="img" aria-label="Photograph of a smiling tradesman in a blue hard hat and overalls, gesturing toward the services list"></div>

    <div class="brand">
      <span class="brand__mark"></span>
      <span class="brand__name">STONEBELL INC</span>
    </div>

    <h1 class="headline headline--question">Water &amp; Air Problems?</h1>
    <p class="headline headline--promise">We Fix It All!</p>

    <ul class="services">
      <li class="services__item">
        <svg class="services__tick" viewBox="0 0 28 28" aria-hidden="true"><circle cx="14" cy="14" r="13" fill="#fff"/><circle cx="14" cy="14" r="10.5" fill="var(--tick)"/><path d="M9 14.5l3.5 3.5 6.5-7" fill="none" stroke="#fff" stroke-width="2.4" stroke-linecap="round" stroke-linejoin="round"/></svg>
        Home Construction &amp; Remodeling
      </li>
      <li class="services__item">
        <svg class="services__tick" viewBox="0 0 28 28" aria-hidden="true"><circle cx="14" cy="14" r="13" fill="#fff"/><circle cx="14" cy="14" r="10.5" fill="var(--tick)"/><path d="M9 14.5l3.5 3.5 6.5-7" fill="none" stroke="#fff" stroke-width="2.4" stroke-linecap="round" stroke-linejoin="round"/></svg>
        HVAC, Humidity &amp; Air Purification
      </li>
      <li class="services__item">
        <svg class="services__tick" viewBox="0 0 28 28" aria-hidden="true"><circle cx="14" cy="14" r="13" fill="#fff"/><circle cx="14" cy="14" r="10.5" fill="var(--tick)"/><path d="M9 14.5l3.5 3.5 6.5-7" fill="none" stroke="#fff" stroke-width="2.4" stroke-linecap="round" stroke-linejoin="round"/></svg>
        Master Plumbing Services
      </li>
      <li class="services__item">
        <svg class="services__tick" viewBox="0 0 28 28" aria-hidden="true"><circle cx="14" cy="14" r="13" fill="#fff"/><circle cx="14" cy="14" r="10.5" fill="var(--tick)"/><path d="M9 14.5l3.5 3.5 6.5-7" fill="none" stroke="#fff" stroke-width="2.4" stroke-linecap="round" stroke-linejoin="round"/></svg>
        Leak Repairs (Roof, Window, Basement)
      </li>
      <li class="services__item">
        <svg class="services__tick" viewBox="0 0 28 28" aria-hidden="true"><circle cx="14" cy="14" r="13" fill="#fff"/><circle cx="14" cy="14" r="10.5" fill="var(--tick)"/><path d="M9 14.5l3.5 3.5 6.5-7" fill="none" stroke="#fff" stroke-width="2.4" stroke-linecap="round" stroke-linejoin="round"/></svg>
        Custom Grading, Drainage &amp; Landscaping
      </li>
    </ul>

    <p class="area">Serving Lynchburg, VA</p>

    <ul class="licenses">
      <li class="licenses__item licenses__item--class">Class A</li>
      <li class="licenses__item licenses__item--hvac">Master HVAC</li>
      <li class="licenses__item licenses__item--plumbing">Master Plumbing</li>
    </ul>

    <div class="phone">
      <svg class="phone__icon" viewBox="0 0 68 68" aria-hidden="true">
        <circle cx="34" cy="34" r="33" fill="#fff"/>
        <circle cx="34" cy="34" r="28" fill="#3a9fe0"/>
        <path d="M25 19c1.5-1 3.5-.6 4.4.9l3 5c.8 1.4.5 3.1-.7 4.1l-2 1.6c1.4 3.4 4.2 6.6 7.6 8.3l1.7-1.9c1-1.2 2.8-1.4 4.1-.5l4.8 3.3c1.4 1 1.8 3 .8 4.4l-1.6 2.3c-1.5 2.2-4.3 3.1-6.8 2.1C29.6 47.3 21.5 39 18.4 28.3c-.7-2.5.3-5.2 2.5-6.6z" fill="#fff"/>
      </svg>
      <span class="phone__number">(434) 555-0182</span>
    </div>
  </section>
</body>
</html>
```